We are in search of a new business card design for our business. We have a Mexican Grocery Store called Tortilla Grove Market, we would like to see that some have mexican design, but we are open to any type of designs.

Phone: to be announced
Fax: to be announced

Address is:
2415 Calloway Blvd
Harlow Point, MD 20614

```html
<!DOCTYPE html>
<html lang="en">
<head>
<meta charset="utf-8">
<title>Tortilla Grove Market – Business Card</title>
<link rel="stylesheet" href="https://fonts.googleapis.com/css2?family=Open+Sans:wght@400;700&display=swap">
<style>
  :root {
    --backdrop: #ece8e3;
    --card: #ffffff;
    --chili-red: #9c1a1c;
    --band-red: #c8232a;
    --band-red-dark: #8e1418;
    --herb-green: #1f7a33;
    --band-green: #238a3c;
    --ink: #222222;
  }
  * { box-sizing: border-box; margin: 0; padding: 0; }
  html, body {
    width: 1200px; height: 1000px; overflow: hidden;
    background: var(--backdrop);
    font-family: "Open Sans", Arial, sans-serif;
  }
  .business-card {
    position: absolute; left: 100px; top: 202px;
    width: 1000px; height: 596px;
    background: var(--card);
    border-radius: 30px;
    overflow: hidden;
    box-shadow: 0 6px 18px rgba(0,0,0,0.12);
  }
  .holder-name {
    position: absolute; left: 50px; top: 90px;
    font-size: 31px; font-weight: 700; letter-spacing: 0.5px; line-height: 42px;
    color: var(--chili-red);
  }
  .holder-title {
    position: absolute; left: 50px; top: 134px;
    font-size: 24px; line-height: 32px; color: var(--herb-green);
  }
  .address {
    position: absolute; left: 50px; top: 212px;
    font-size: 24px; line-height: 31px; color: var(--ink);
    font-style: normal;
  }
  .contact-list {
    position: absolute; left: 50px; top: 296px;
    list-style: none; font-size: 24px; line-height: 34px; color: var(--ink);
  }
  .contact-list li { display: flex; align-items: center; gap: 8px; }
  .contact-icon { width: 22px; height: 22px; fill: var(--band-red); flex: none; }
  .brand-mark {
    position: absolute; left: 560px; top: 150px; width: 380px;
    display: flex; flex-direction: column; align-items: center; gap: 14px;
  }
  .brand-dot {
    width: 46px; height: 46px; border-radius: 50%; background: var(--band-red);
  }
  .brand-name {
    font-size: 44px; font-weight: 700; line-height: 50px; text-align: center;
    color: var(--chili-red);
  }
  .ribbon-area {
    position: absolute; left: 0; top: 470px; width: 1000px; height: 80px;
    background: linear-gradient(90deg, var(--band-red) 0%, var(--band-red-dark) 55%, var(--band-green) 100%);
    opacity: 0.85;
  }
</style>
</head>
<body>
  <article class="business-card">
    <h1 class="holder-name">MARCO R. DELVANE</h1>
    <p class="holder-title">Managing Director</p>

    <address class="address">2415 Calloway Blvd<br>Harlow Point, MD 20614</address>

    <ul class="contact-list">
      <li><svg class="contact-icon" viewBox="0 0 24 24"><path d="M3 9c0-3 4-5 9-5s9 2 9 5l-3 1-2-3H8L6 10zM6 11h12l2 8H4z"/></svg>+ 000 000 0000</li>
      <li><svg class="contact-icon" viewBox="0 0 24 24"><path d="M7 3h10v5H7zM3 9h18v8h-3v-3H6v3H3zM7 15h10v6H7z"/></svg>+ 000 000 0000</li>
      <li><svg class="contact-icon" viewBox="0 0 24 24"><path d="M2 5h20v14H2zM3 6l9 7 9-7v2l-9 7-9-7z" fill-rule="evenodd"/></svg>info@tortillagrovemarket.com</li>
      <li><svg class="contact-icon" viewBox="0 0 24 24"><circle cx="11" cy="12" r="9"/><path d="M13 12l8 4-3 1 3 3-2 2-3-3-1 3z" fill="#fff"/></svg>www.tortillagrovemarket.com</li>
    </ul>

    <div class="brand-mark">
      <span class="brand-dot" aria-hidden="true"></span>
      <p class="brand-name">Tortilla Grove<br>Market</p>
    </div>

    <div class="ribbon-area" role="img" aria-label="Decorative red and green flowing ribbon along the bottom of the card"></div>
  </article>
</body>
</html>
```